I need a Label design for my tavin 58 kombucha brand that is launching soon

I want a label to go on my tavin 58 kombucha bottle.
I have a logo image uploaded in the files but I am open to changes to this logo or even a completely New one if you think you can do better. This logo is based on the idea of an s-shaped naga. I particularly like the nagas from temples in luang prabang.
I also want to include the slogan - dare to be delicious.
The label should be some kind of oval at 80mm high by 70mm wide.
The label will go on a clear glass bottle. The kombucha will be visible and comes in different shades of red,yellow and purple.
The word kombucha should be clearly visible.
i want a very colorful, playful label. I'm very keen to see your ideas and I want something original.
Fermented foods and beverages

```html
<!DOCTYPE html>
<html lang="en">
<head>
<meta charset="utf-8">
<title>tavin 58 Kombucha – Oval Label</title>
<link rel="stylesheet" href="https://fonts.googleapis.com/css2?family=Anton&family=Josefin+Sans:wght@300&family=Poppins:wght@800&display=swap">
<style>
  :root {
    --backdrop: #d9d9d9;
    --label-white: #ffffff;
    --label-dark: #262628;
    --brand-magenta: #c22b7a;
    --brand-grey: #5c5c60;
    --ink-black: #1e1e20;
    --rainbow-red: #e0412f;
    --rainbow-orange: #ec6b2a;
    --rainbow-amber: #f39a25;
    --rainbow-yellow: #f3c326;
    --rainbow-lime: #b2c63c;
    --rainbow-green: #6bb64a;
    --rainbow-teal: #4bb5b0;
    --rainbow-blue: #5fa6d6;
    --rainbow-purple: #9c5aa6;
  }
  * { margin: 0; padding: 0; box-sizing: border-box; }
  html, body {
    width: 828px; height: 1200px; overflow: hidden;
    background: var(--backdrop);
  }
  .label {
    position: relative;
    width: 828px; height: 1200px;
  }
  .label-art { position: absolute; inset: 0; }
  .brand-mark {
    position: absolute; left: 0; right: 0; top: 392px;
    text-align: center;
    font-family: "Josefin Sans", sans-serif;
    font-weight: 300;
    color: var(--brand-grey);
  }
  .brand-name {
    display: block;
    font-size: 104px; line-height: 84px;
    letter-spacing: -2px;
  }
  .brand-number {
    display: inline-flex; align-items: center; gap: 14px;
    font-size: 62px; line-height: 60px;
    margin-top: 2px;
  }
  .brand-number::before, .brand-number::after {
    content: ""; display: block; width: 104px; height: 2px;
    background: var(--brand-grey);
  }
  .kombucha-word {
    font-family: "Anton", sans-serif;
    font-size: 150px;
    fill: var(--ink-black);
    stroke: var(--label-white);
    stroke-width: 9px;
    paint-order: stroke fill;
    stroke-linejoin: round;
  }
  .slogan-lead {
    font-family: "Poppins", sans-serif;
    font-size: 38px;
    fill: var(--label-white);
  }
  .slogan-word {
    font-family: "Poppins", sans-serif;
    font-size: 60px;
    stroke: var(--label-white);
    stroke-width: 6px;
    paint-order: stroke fill;
    stroke-linejoin: round;
  }
</style>
</head>
<body>
<main class="label">
  <svg class="label-art" width="828" height="1200" viewBox="0 0 828 1200" xmlns="http://www.w3.org/2000/svg">
    <defs>
      <clipPath id="label-inner">
        <ellipse cx="415" cy="601" rx="362" ry="414"/>
      </clipPath>
      <linearGradient id="splash-tones" x1="0" x2="1" y1="0" y2="0">
        <stop offset="0" stop-color="#e0412f"/>
        <stop offset="0.3" stop-color="#f39a25"/>
        <stop offset="0.55" stop-color="#8cc63f"/>
        <stop offset="0.8" stop-color="#4bb5d6"/>
        <stop offset="1" stop-color="#d34b8f"/>
      </linearGradient>
    </defs>

    <ellipse class="label-rim" cx="414" cy="600" rx="382" ry="436" fill="var(--label-white)"/>
    <ellipse class="label-body" cx="415" cy="601" rx="362" ry="414" fill="var(--label-dark)"/>

    <g clip-path="url(#label-inner)">
      <path class="label-band" fill="var(--brand-magenta)"
            d="M40 505 Q415 640 790 505 L790 820 Q740 800 690 790 L700 830
               Q560 750 415 752 Q270 750 130 830 L140 790 Q90 800 40 820 Z"/>
    </g>

    <circle class="brand-dot" cx="414" cy="300" r="62" fill="var(--brand-magenta)"/>

    <text class="kombucha-word" x="415" y="732" text-anchor="middle" textLength="620" lengthAdjust="spacingAndGlyphs">KOMBUCHA</text>

    <text class="slogan-lead" x="414" y="846" text-anchor="middle" textLength="270" lengthAdjust="spacingAndGlyphs">DARE TO BE</text>

    <text class="slogan-word" x="414" y="918" text-anchor="middle" textLength="360" lengthAdjust="spacingAndGlyphs"><tspan fill="var(--rainbow-red)">D</tspan><tspan fill="var(--rainbow-orange)">E</tspan><tspan fill="var(--rainbow-amber)">L</tspan><tspan fill="var(--rainbow-yellow)">I</tspan><tspan fill="var(--rainbow-lime)">C</tspan><tspan fill="var(--rainbow-green)">I</tspan><tspan fill="var(--rainbow-teal)">O</tspan><tspan fill="var(--rainbow-blue)">U</tspan><tspan fill="var(--rainbow-purple)">S</tspan></text>

    <rect class="slogan-splash" role="img" aria-label="Colourful paint splash ornament"
          x="332" y="934" width="176" height="44" rx="22" fill="url(#splash-tones)"/>
  </svg>

  <div class="brand-mark">
    <span class="brand-name">tavin</span>
    <span class="brand-number">58</span>
  </div>
</main>
</body>
</html>
```